Packing for a Vodka Fruit Mix Drink wanted!

We are looking for a modern and elegant design for the packaging of a Vodka Fruit Mix Drink. The drink is filled into a 100ml (90 x 145 mm) SpoutBag (Veltrisa) and shoulderstand be sold in different varieties. The packaging shoulderstand be very plain, simple and modern. Less is more! The logo Should be Placed large and centrally. The background shoulderstand be dark. - But if a bright background is more effective, You Could convince us. In addition, the types of fruit and vodka shoulderstand be read. (Eg Mango - Pineapple - Vodka) There will be in the future, different varieties, there Should be a color scheme for the various varieties. Each variety shoulderstand be Recognized equal to the shelf. (For example, lines of different colors, denominations, ...) Font: http://www.glyphmarket-example.com/search.html?search=tornelle&x=0&y=0
Reason: I am on holiday till 18. May

```html
<!DOCTYPE html>
<html lang="en">
<head>
<meta charset="utf-8">
<title>Fenric Grove – Vodka Spout Pouch Range</title>
<link rel="stylesheet" href="https://fonts.googleapis.com/css2?family=Orbitron:wght@400;500&display=swap">
<style>
  :root {
    --backdrop: #e4e5e7;
    --pouch-black: #1b1b1c;
    --pouch-pattern-a: #2a2a2b;
    --pouch-pattern-b: #161617;
    --cap-white: #f4f4f4;
    --cap-shade: #d6d6d6;
    --ink-white: #f2f2f2;
    --ink-dark: #141414;
    --ink-grey: #9a9a9a;
    --orange: #f39420;
    --apple: #8cc63f;
    --pineapple: #ffdd1a;
  }
  * { box-sizing: border-box; margin: 0; padding: 0; }
  html, body { width: 1200px; height: 860px; overflow: hidden; }
  body {
    background: var(--backdrop);
    font-family: "Orbitron", "Arial", sans-serif;
  }
  .range {
    position: relative;
    width: 1200px;
    height: 860px;
    display: flex;
    justify-content: center;
    align-items: flex-start;
    gap: 36px;
    padding-top: 110px;
  }
  .pouch {
    position: relative;
    width: 330px;
    display: flex;
    flex-direction: column;
    align-items: center;
  }
  .spout-cap {
    width: 84px;
    height: 62px;
    border-radius: 4px 4px 0 0;
    background: repeating-linear-gradient(90deg, var(--cap-white) 0 5px, var(--cap-shade) 5px 7px);
  }
  .spout-collar {
    width: 100px;
    height: 22px;
    background: var(--cap-white);
    border-radius: 3px;
    box-shadow: inset 0 -3px 0 var(--cap-shade);
  }
  .pouch-body {
    position: relative;
    width: 330px;
    height: 580px;
    margin-top: -4px;
    border-radius: 26px 26px 12px 12px;
    background: var(--pouch-black);
    overflow: hidden;
    display: flex;
    flex-direction: column;
    align-items: center;
  }
  .pouch-pattern {
    position: absolute;
    inset: 0;
    background: linear-gradient(160deg, var(--pouch-pattern-a), var(--pouch-pattern-b) 70%);
  }
  .brand {
    position: relative;
    margin-top: 66px;
    display: flex;
    flex-direction: column;
    align-items: center;
  }
  .brand-disc {
    width: 150px;
    height: 150px;
    border: 4px solid var(--ink-white);
    border-radius: 50%;
  }
  .brand-name {
    margin-top: 34px;
    color: var(--ink-white);
    font-weight: 400;
    font-size: 36px;
    line-height: 1.15;
    letter-spacing: 2px;
    text-align: center;
    text-transform: uppercase;
  }
  .variety-band {
    position: relative;
    margin-top: 42px;
    width: 100%;
    height: 78px;
    display: flex;
    flex-direction: column;
    justify-content: center;
    align-items: center;
    color: var(--ink-dark);
    font-weight: 500;
    font-size: 24px;
    line-height: 1.1;
  }
  .variety-band .spirit { text-transform: uppercase; letter-spacing: 1px; }
  .variety-band.is-orange { background: var(--orange); }
  .variety-band.is-apple { background: var(--apple); }
  .variety-band.is-pineapple { background: var(--pineapple); }
  .volume {
    position: absolute;
    bottom: 58px;
    color: var(--ink-grey);
    font-size: 13px;
    letter-spacing: 1px;
  }
</style>
</head>
<body>
<main class="range">

  <article class="pouch">
    <div class="spout-cap"></div>
    <div class="spout-collar"></div>
    <div class="pouch-body">
      <div class="pouch-pattern" role="img" aria-label="Dark charcoal chevron maze pattern across the pouch"></div>
      <div class="brand">
        <div class="brand-disc"></div>
        <p class="brand-name">Fenric<br>Grove</p>
      </div>
      <div class="variety-band is-orange">
        <span class="fruit">Orange</span>
        <span class="spirit">Vodka</span>
      </div>
      <p class="volume">100mL</p>
    </div>
  </article>

  <article class="pouch">
    <div class="spout-cap"></div>
    <div class="spout-collar"></div>
    <div class="pouch-body">
      <div class="pouch-pattern" role="img" aria-label="Dark charcoal chevron maze pattern across the pouch"></div>
      <div class="brand">
        <div class="brand-disc"></div>
        <p class="brand-name">Fenric<br>Grove</p>
      </div>
      <div class="variety-band is-apple">
        <span class="fruit">Apple</span>
        <span class="spirit">Vodka</span>
      </div>
      <p class="volume">100mL</p>
    </div>
  </article>

  <article class="pouch">
    <div class="spout-cap"></div>
    <div class="spout-collar"></div>
    <div class="pouch-body">
      <div class="pouch-pattern" role="img" aria-label="Dark charcoal chevron maze pattern across the pouch"></div>
      <div class="brand">
        <div class="brand-disc"></div>
        <p class="brand-name">Fenric<br>Grove</p>
      </div>
      <div class="variety-band is-pineapple">
        <span class="fruit">Pineapple</span>
        <span class="spirit">Vodka</span>
      </div>
      <p class="volume">100mL</p>
    </div>
  </article>

</main>
</body>
</html>
```